Tech Company New PowerPoint Design Project

We are an IT Managed services, cloud and cyber security company https://www.korvanti.com.au/ Requesting proposals for a PowerPoint deck template that can be used by our sales team when pitching clients, our head office is located in Australa and we do have regional offices in NZ , USA , SRI LANKA and SINGAPORE. and also required to have a proposal/SOW template created too (not sure if this is something that we can include to this proposal) we may need a lot of things done in future but this is where i like to get started for now.. please let m eknow your thoughts and if you have any questions.
Target Market(s)
Enterprise
Industry/Entity Type
Information Technology

```html
<!DOCTYPE html>
<html lang="en">
<head>
<meta charset="utf-8">
<title>Korvanti – Sales Deck</title>
<link href="https://fonts.googleapis.com/css2?family=Exo+2:wght@400;500;600;700&family=Roboto:wght@400;500&display=swap" rel="stylesheet">
<style>
:root{
  --page:#ebebeb;
  --navy:#0a1330;
  --navy-deep:#050a1c;
  --brand:#1a9ad6;
  --brand-light:#cfe6f4;
  --ink:#0b0b16;
  --body:#555a66;
  --footer:#050505;
  --white:#ffffff;
  --card-shadow:rgba(20,40,80,.10);
  --map:#e9c9c4;
}
*{box-sizing:border-box;margin:0;padding:0}
html,body{width:1200px;height:4110px;overflow:hidden}
body{background:var(--page);position:relative;font-family:"Roboto",sans-serif;color:var(--body)}
.slide{position:absolute;left:65px;width:1070px;height:602px;background:var(--white);overflow:hidden;box-shadow:0 2px 10px rgba(0,0,0,.05)}
.slide--dark{background:linear-gradient(100deg,var(--navy-deep) 0%,var(--navy) 55%,#0e1f42 100%)}
.brand{font-family:"Exo 2",sans-serif;font-weight:400;color:var(--brand);letter-spacing:1px;position:absolute}
.hero-title{position:absolute;left:77px;font-family:"Exo 2",sans-serif;font-weight:600;color:var(--white);line-height:1.15}
.tagline{position:absolute;left:77px;font-family:"Exo 2",sans-serif;font-weight:500;color:var(--brand);font-size:20px}
.web-pill{position:absolute;left:78px;height:37px;width:214px;border-radius:19px;background:var(--brand);color:var(--white);font-size:13px;letter-spacing:2px;display:flex;align-items:center;padding-left:12px;gap:12px}
.web-pill svg{flex:none}
.photo{position:absolute}
/* content slide frame */
.slide-title{position:absolute;left:54px;top:44px;font-family:"Exo 2",sans-serif;font-weight:700;font-size:40px;color:var(--ink)}
.slide .brand--head{right:54px;top:40px;font-size:44px}
.rule{position:absolute;left:0;right:0;top:115px;height:1px;background:var(--brand-light)}
.rule-accent{position:absolute;left:54px;top:113px;width:48px;height:6px;border-radius:3px;background:var(--brand)}
.footer{position:absolute;left:0;right:0;bottom:0;height:42px;background:var(--footer);color:var(--white);font-size:10px;display:flex;align-items:center;padding-left:54px}
.footer a{color:var(--brand);text-decoration:underline}
.footer .page-no{position:absolute;right:0;top:0;height:42px;width:181px;background:var(--brand);display:flex;align-items:center;justify-content:center;font-size:10px}
/* contents */
.toc-item{position:absolute;width:420px}
.toc-icon{position:absolute;left:0;top:0;width:62px;height:62px;border-radius:50%;background:var(--brand);box-shadow:0 0 0 4px #d8ecf8;display:flex;align-items:center;justify-content:center}
.toc-item h3{position:absolute;left:84px;top:2px;font-family:"Exo 2",sans-serif;font-weight:600;font-size:20px;color:var(--ink)}
.toc-item p{position:absolute;left:84px;top:34px;width:345px;font-size:10px;line-height:18px;color:var(--body)}
/* who we are */
.about-lead{position:absolute;left:535px;top:144px;width:480px;font-size:12px;line-height:24px;text-align:justify}
.about-list{position:absolute;left:541px;top:283px;width:474px;list-style:none}
.about-list li{position:relative;padding-left:28px;font-size:10.5px;line-height:21px;margin-bottom:21px}
.about-list svg{position:absolute;left:0;top:3px}
/* offer cards */
.offer{position:absolute;width:311px;height:158px;background:var(--white);border-radius:10px;box-shadow:0 4px 18px var(--card-shadow)}
.offer svg{position:absolute;left:16px;top:24px}
.offer h3{position:absolute;left:66px;top:22px;font-family:"Exo 2",sans-serif;font-weight:500;font-size:18px;color:var(--ink)}
.offer p{position:absolute;left:67px;top:52px;width:228px;font-size:10.5px;line-height:19px}
/* locations */
.world{position:absolute;left:174px;top:182px;width:730px;height:324px;border-radius:40px;background:radial-gradient(ellipse at 50% 45%,#f2dcd8 0%,#f7ebe9 60%,rgba(255,255,255,0) 80%)}
.pin{position:absolute;font-size:10px;font-weight:500;color:var(--ink)}
.pin svg{display:block;margin-bottom:2px}
/* thank you */
.thanks-art{position:absolute;left:480px;top:0;width:590px;height:602px;background:radial-gradient(circle at 60% 55%,#c46a25 0%,#2c6a7d 22%,#0d2c48 45%,rgba(10,19,48,0) 75%)}
.follow{position:absolute;left:77px;top:459px;display:flex;align-items:center;gap:6px;color:var(--white);font-family:"Exo 2",sans-serif;font-weight:600;font-size:20px}
.follow span.dot{width:27px;height:27px;border-radius:50%;background:var(--brand);display:inline-block}
.follow .label{margin-right:8px}
</style>
</head>
<body>

<!-- 1: welcome -->
<section class="slide slide--dark" style="top:64px">
  <div class="photo" role="img" aria-label="Two IT engineers reviewing a laptop in a server room" style="left:480px;top:0;width:590px;height:602px;background:linear-gradient(90deg,rgba(10,19,48,0) 0%,#2a2a34 25%,#6b5a4a 60%,#3a3a44 100%)"></div>
  <div class="brand" style="left:77px;top:90px;font-size:50px">korvanti</div>
  <h1 class="hero-title" style="top:270px;font-size:50px">Welcome To<br>Korvanti</h1>
  <div class="tagline" style="top:405px">IT Managed services</div>
  <div class="web-pill" style="top:458px">
    <svg width="18" height="18" viewBox="0 0 18 18"><circle cx="9" cy="9" r="8" fill="#fff"/><path d="M5 5c2 1 3 3 2 5s1 3 2 5M11 3c0 2 2 2 3 4" stroke="#1a9ad6" stroke-width="1.5" fill="none"/></svg>
    www.korvanti.com.au
  </div>
</section>

<!-- 2: contents -->
<section class="slide" style="top:740px">
  <h2 class="slide-title">Table Of Contents</h2>
  <div class="brand brand--head">korvanti</div>
  <div class="rule"></div><div class="rule-accent"></div>

  <div class="toc-item" style="left:80px;top:170px">
    <div class="toc-icon"><svg width="30" height="30" viewBox="0 0 30 30" fill="none" stroke="#fff" stroke-width="1.6"><path d="M15 7a7 7 0 0 0-4 12.7V22h8v-2.3A7 7 0 0 0 15 7z"/><path d="M12 25h6M15 2v2M5 6l1.5 1.5M25 6l-1.5 1.5M2 15h2M26 15h2"/></svg></div>
    <h3>Introduction</h3>
    <p>Ensuring your requirements are met in order to strengthen &amp; enhance your business to a whole new level.</p>
  </div>
  <div class="toc-item" style="left:560px;top:170px">
    <div class="toc-icon"><svg width="30" height="30" viewBox="0 0 30 30" fill="none" stroke="#fff" stroke-width="1.6"><path d="M5 25l11-11M20 4a5 5 0 0 0-5 6l-2 2 4 4 2-2a5 5 0 0 0 6-5l-3 3-3-1-1-3z"/><path d="M6 5l6 6M4 7l3-3M17 19l6 6-2 2-6-6"/></svg></div>
    <h3>What We Offer</h3>
    <p>Our support consists of great IT Services and a Passionate customer service TEAM to make sure you operate</p>
  </div>
  <div class="toc-item" style="left:80px;top:287px">
    <div class="toc-icon"><svg width="30" height="30" viewBox="0 0 30 30" fill="none" stroke="#fff" stroke-width="1.6"><rect x="4" y="6" width="22" height="19" rx="2"/><path d="M4 11h22M10 3v5M20 3v5M8 15h3M13.5 15h3M19 15h3M8 19h3M13.5 19h3M19 19h3"/></svg></div>
    <h3>Agenda</h3>
    <p>Whether you need support for integration or ongoing operational services, KORVANTI has the insight and technical capability to deliver.</p>
  </div>
  <div class="toc-item" style="left:560px;top:287px">
    <div class="toc-icon"><svg width="30" height="30" viewBox="0 0 30 30" fill="none" stroke="#fff" stroke-width="1.6"><path d="M4 9l7-3 8 3 7-3v16l-7 3-8-3-7 3z"/><path d="M11 6v16M19 9v16"/><circle cx="15" cy="13" r="2.5"/></svg></div>
    <h3>Our Locations</h3>
    <p>our head office is located in Australia and we do have regional offices in NZ , USA , SRI LANKA and SINGAPORE.</p>
  </div>
  <div class="toc-item" style="left:80px;top:404px">
    <div class="toc-icon"><svg width="30" height="30" viewBox="0 0 30 30" fill="none" stroke="#fff" stroke-width="1.6"><circle cx="14" cy="16" r="10"/><circle cx="14" cy="16" r="5.5"/><circle cx="14" cy="16" r="1.5"/><path d="M14 16l11-11M21 5h4v4"/></svg></div>
    <h3>Who We Are</h3>
    <p>While there are many businesses providing the same services, what we deliver is unparalleled. Whether services or solutions.</p>
  </div>
  <div class="toc-item" style="left:560px;top:404px">
    <div class="toc-icon"><svg width="30" height="30" viewBox="0 0 30 30" fill="none" stroke="#fff" stroke-width="1.8"><circle cx="15" cy="15" r="11"/><path d="M10 15l4 4 7-8"/></svg></div>
    <h3>Thank You</h3>
    <p>Whether services or solutions, we keep standing with our clients through thick and thin.</p>
  </div>

  <footer class="footer">(C) Copyright 2024&nbsp;<a>Korvanti</a>&nbsp;| All Rights Reserved<span class="page-no">Page 02 Of 06</span></footer>
</section>

<!-- 3: who we are -->
<section class="slide" style="top:1408px">
  <h2 class="slide-title">Who We Are</h2>
  <div class="brand brand--head">korvanti</div>
  <div class="rule"></div><div class="rule-accent"></div>

  <div class="photo" role="img" aria-label="Two colleagues reviewing a tablet in a data centre" style="left:54px;top:158px;width:444px;height:358px;border-radius:22px;background:linear-gradient(135deg,#33475e 0%,#6f8196 45%,#b9c4d2 70%,#2b3a50 100%)"></div>

  <p class="about-lead">KORVANTI is a one-stop destination for all your IT Management Requirements. We are committed to delivering cutting-edge, simplified IT solutions through our highly skilled team and flexible engagement models. Whether you need support for integration or ongoing operational services, KORVANTI has the insight and technical capability to deliver simplified solutions.</p>
  <ul class="about-list">
    <li><svg width="16" height="16" viewBox="0 0 16 16" fill="none" stroke="#1a9ad6" stroke-width="1.6"><circle cx="8" cy="8" r="6.5"/><path d="M5 8l2.5 2.5L14 3"/></svg>Our passion, enthusiasm, and value are what make us different from our peers. While there are many businesses providing the same services, what we deliver is unparalleled. Whether services or solutions, we keep standing with our clients through thick and thin.</li>
    <li><svg width="16" height="16" viewBox="0 0 16 16" fill="none" stroke="#1a9ad6" stroke-width="1.6"><circle cx="8" cy="8" r="6.5"/><path d="M5 8l2.5 2.5L14 3"/></svg>Whether you need support for integration or ongoing operational services, KORVANTI has the insight and technical capability to deliver simplified solutions.</li>
    <li><svg width="16" height="16" viewBox="0 0 16 16" fill="none" stroke="#1a9ad6" stroke-width="1.6"><circle cx="8" cy="8" r="6.5"/><path d="M5 8l2.5 2.5L14 3"/></svg>Being an Australian based organization, we are 100% Customer Focused and provide innovative and flexible IT services and simple solutions that enhance business productivity. We pride ourselves on the flexibility in our approach.</li>
  </ul>

  <footer class="footer">(C) Copyright 2024&nbsp;<a>Korvanti</a>&nbsp;| All Rights Reserved<span class="page-no">Page 03 Of 06</span></footer>
</section>

<!-- 4: what we offer -->
<section class="slide" style="top:2076px">
  <h2 class="slide-title">What We Offer</h2>
  <div class="brand brand--head">korvanti</div>
  <div class="rule"></div><div class="rule-accent"></div>

  <article class="offer" style="left:40px;top:160px">
    <svg width="38" height="38" viewBox="0 0 38 38" fill="none" stroke="#1a9ad6" stroke-width="1.5"><circle cx="24" cy="8" r="4"/><path d="M17 20a7 7 0 0 1 14 0"/><rect x="4" y="16" width="12" height="9"/><path d="M2 27h34M6 27v8M32 27v8M8 31h22"/></svg>
    <h3>Managed Service Desk</h3>
    <p>Single point of contact for incident and service request handling &amp; remote support including a fixed monthly rate with unlimited support under service level agreements</p>
  </article>
  <article class="offer" style="left:378px;top:160px">
    <svg width="38" height="38" viewBox="0 0 38 38" fill="none" stroke="#1a9ad6" stroke-width="1.5"><rect x="3" y="5" width="32" height="22" rx="2"/><path d="M14 33h10M19 27v6M13 12l-4 4 4 4M25 12l4 4-4 4M21 11l-4 10"/></svg>
    <h3>Software Development</h3>
    <p>Builds innovative enterprise systems, software solutions and automation solutions with managed support services</p>
  </article>
  <article class="offer" style="left:717px;top:160px">
    <svg width="38" height="38" viewBox="0 0 38 38" fill="none" stroke="#1a9ad6" stroke-width="1.5"><rect x="13" y="8" width="12" height="6" rx="1"/><rect x="13" y="16" width="12" height="6" rx="1"/><rect x="13" y="24" width="12" height="6" rx="1"/><path d="M13 11H6M13 27H6M25 19h7M6 11v16"/><circle cx="6" cy="19" r="2"/><circle cx="33" cy="19" r="2"/></svg>
    <h3>It Consulting</h3>
    <p>Link your technical stress with smart consulting ethics and then provide ideas and solutions for analyzing and diagnosing the company's IT infrastructure</p>
  </article>
  <article class="offer" style="left:40px;top:338px">
    <svg width="38" height="38" viewBox="0 0 38 38" fill="none" stroke="#1a9ad6" stroke-width="1.5"><path d="M19 8l9 3v8c0 6-4 9-9 11-5-2-9-5-9-11v-8z"/><rect x="15" y="18" width="8" height="6"/><path d="M16.5 18v-2a2.5 2.5 0 0 1 5 0v2M19 1v4M19 33v4M1 19h5M32 19h5M6 6l3 3M29 29l3 3M32 6l-3 3M6 32l3-3"/></svg>
    <h3>Cyber Security Support</h3>
    <p>The KORVANTI SOC Team provides large-scale Cyber Security Coverage for organizations to protect their Confidentiality, Integrity, and Availability (CIA).</p>
  </article>
  <article class="offer" style="left:378px;top:338px">
    <svg width="38" height="38" viewBox="0 0 38 38" fill="none" stroke="#1a9ad6" stroke-width="1.5"><circle cx="19" cy="10" r="5"/><path d="M19 3v2M19 15v2M12 10h2M24 10h2"/><rect x="3" y="22" width="14" height="12"/><rect x="21" y="22" width="14" height="12"/><path d="M3 26h14M21 26h14M19 17v5"/></svg>
    <h3>Procurement Services</h3>
    <p>Supply or consult on all hardware aspects of any network. If you're searching for a new PC, Laptop, considering increasing your available storage</p>
  </article>

  <footer class="footer">(C) Copyright 2024&nbsp;<a>Korvanti</a>&nbsp;| All Rights Reserved<span class="page-no">Page 04 Of 06</span></footer>
</section>

<!-- 5: locations -->
<section class="slide" style="top:2743px">
  <h2 class="slide-title">Our Locations</h2>
  <div class="brand brand--head">korvanti</div>
  <div class="rule"></div><div class="rule-accent"></div>

  <div class="world" role="img" aria-label="Dotted world map showing regional office locations"></div>

  <div class="pin" style="left:272px;top:263px">
    <svg width="16" height="16" viewBox="0 0 16 16"><path d="M7 0h2v16H7z" fill="#1a9ad6"/><path d="M2 3h12l2 2-2 2H2zM0 9h12v4H2z" fill="#1a9ad6"/></svg>USA</div>
  <div class="pin" style="left:704px;top:361px">
    <svg width="16" height="16" viewBox="0 0 16 16" style="margin-left:38px"><path d="M7 0h2v16H7z" fill="#1a9ad6"/><path d="M2 3h12l2 2-2 2H2zM0 9h12v4H2z" fill="#1a9ad6"/></svg>Singapore</div>
  <div class="pin" style="left:568px;top:428px">
    <svg width="16" height="16" viewBox="0 0 16 16"><path d="M7 0h2v16H7z" fill="#1a9ad6"/><path d="M2 3h12l2 2-2 2H2zM0 9h12v4H2z" fill="#1a9ad6"/></svg>Sri Lanka</div>
  <div class="pin" style="left:873px;top:450px">
    <svg width="16" height="16" viewBox="0 0 16 16"><path d="M7 0h2v16H7z" fill="#1a9ad6"/><path d="M2 3h12l2 2-2 2H2zM0 9h12v4H2z" fill="#1a9ad6"/></svg>New Zealand</div>

  <footer class="footer">(C) Copyright 2024&nbsp;<a>Korvanti</a>&nbsp;| All Rights Reserved<span class="page-no">Page 05 Of 06</span></footer>
</section>

<!-- 6: thank you -->
<section class="slide slide--dark" style="top:3447px">
  <div class="thanks-art" role="img" aria-label="Glowing digital security shield with keyhole on a circuit background"></div>
  <div class="brand" style="left:77px;top:112px;font-size:50px">korvanti</div>
  <h2 class="hero-title" style="top:318px;font-size:58px">Thank You</h2>
  <div class="web-pill" style="top:399px">
    <svg width="18" height="18" viewBox="0 0 18 18"><circle cx="9" cy="9" r="8" fill="#fff"/><path d="M5 5c2 1 3 3 2 5s1 3 2 5M11 3c0 2 2 2 3 4" stroke="#1a9ad6" stroke-width="1.5" fill="none"/></svg>
    www.korvanti.com.au
  </div>
  <div class="follow"><span class="label">Follow Us:</span><span class="dot"></span><span class="dot"></span><span class="dot"></span></div>
</section>

</body>
</html>
```